Design a brochure for Tavren Chiropractic

Dear Freelancers.

I would like to design a brochure for me in Microsoft publisher format ( so I can edit it myself ) for my mobile Chiropractic Business “ Tavren Chiropractic “
You can get a good idea of the color and font themes on the website here
I have also included a draft design that a freelancer did for me in Adobe Illustration ( marked draft 1 and 2 ) I like some of the design layout but I really think I am going to need a publisher version so I can make my own revisions.

I would also like a more professional corporate look than this flyer suggests so I decided not to push on a instead offer this as a contest.

I am thinking we go for a trifold A4 design. I have scanned a ( badly ! ) hand-drawn layout with a suggested idea but this is not set in stone. If you have any better ideas on layout please let me know and we can try and get it right together. You are the expert here and I would love this to look amazing. Because I am mobile I really need this project the right image.
I’m thinking we go with a very faded image background or white background but also open to use of faded photo’ particularly on the front cover. At any rate I guess we need to stick with the blue and white themed of the website but again if you have any ideas happy to hear them. Again I want this service to appeal to wealthy clients so the layout and design should be classy and very professional. Feel free to ask me anything that is not clear.
I also wish to be able to take it to printers and not have any borders on the print output. I always struggle with this when I try to make my own publisher documents.

It’s a bit hard for me to tell how much text will actually fit and I know most graphic designers usually like to tell their clients to use less so I would value your judgement on how much info we can fit here but I guess we have to start somewhere ?

I have split the design into 6 sections (for an A4 trifold ) and the text you will that we can try to fit into each section is below.

You can find all the images and documents you need here

[login to view URL]!BqwK4jLdx-7mnEsY-pkfaWJr2TtsHM

Further information can be found on the attached word document

```html
<!DOCTYPE html>
<html lang="en">
<head>
<meta charset="utf-8">
<title>Tavren Chiropractic – Trifold Brochure</title>
<link href="https://fonts.googleapis.com/css2?family=Cinzel:wght@400;600&family=Roboto:wght@400;500;700&display=swap" rel="stylesheet">
<style>
  :root {
    --page-bg: #dfe3e7;
    --paper: #ffffff;
    --teal: #2bb2c8;
    --teal-light: #d9f1f5;
    --navy: #1f5d93;
    --title-blue: #1d4f82;
    --ink: #1f2a33;
    --mountain-top: #eef3f8;
    --mountain-base: #3e6fa8;
  }
  * { box-sizing: border-box; margin: 0; padding: 0; }
  html, body { width: 1200px; height: 800px; overflow: hidden; }
  body { background: var(--page-bg); font-family: "Roboto", sans-serif; color: var(--ink); position: relative; }

  .brochure { position: absolute; left: 77px; top: 20px; width: 1046px; height: 760px; background: var(--paper); box-shadow: 0 6px 24px rgba(0,0,0,.18); overflow: hidden; }
  .fold { position: absolute; top: 0; bottom: 0; width: 1px; background: rgba(0,0,0,.06); }

  /* Left panel */
  .welcome { position: absolute; left: 0; width: 362px; top: 48px; text-align: center; font-family: "Cinzel", serif; color: var(--teal); font-size: 21px; letter-spacing: 1px; }
  .brand-name { position: absolute; left: 0; width: 362px; top: 80px; text-align: center; font-family: "Cinzel", serif; font-weight: 600; color: var(--title-blue); font-size: 38px; line-height: 1; letter-spacing: 1px; }
  .brand-sub { position: absolute; left: 0; width: 362px; top: 128px; text-align: center; font-family: "Cinzel", serif; font-weight: 600; color: var(--title-blue); font-size: 14px; letter-spacing: 4px; }

  .values { position: absolute; left: 12px; top: 172px; width: 350px; height: 232px; background: var(--navy); color: #fff; padding: 14px 22px 0 22px; }
  .values h2 { font-weight: 500; font-size: 23px; margin-bottom: 8px; }
  .values p { font-size: 12.4px; line-height: 16px; text-align: justify; }

  .pill { position: absolute; background: var(--teal); color: #fff; border-radius: 20px; text-align: center; font-weight: 500; }
  .give-title { left: 88px; top: 434px; width: 186px; height: 34px; line-height: 34px; font-size: 20px; }

  .benefits { position: absolute; left: 30px; top: 484px; width: 318px; display: flex; justify-content: space-between; }
  .benefit { color: var(--teal); font-size: 11.5px; font-weight: 500; line-height: 14px; white-space: nowrap; }
  .benefit.care { width: 88px; }
  .benefit.timing { width: 88px; }
  .benefit.quality { width: 132px; }
  .benefit svg { display: block; margin: 0 0 8px 14px; }

  .book-band { position: absolute; left: 0; top: 600px; width: 362px; height: 18px; }
  .book-band .rule { position: absolute; top: 7px; height: 4px; background: var(--teal); }
  .book-band .label { position: absolute; left: 110px; width: 150px; top: 0; height: 18px; line-height: 18px; background: var(--teal); color: #fff; font-size: 13px; font-weight: 500; text-align: center; }
  .book-text { position: absolute; left: 0; width: 362px; top: 630px; text-align: center; font-size: 13px; font-weight: 500; line-height: 17px; }
  .book-link { position: absolute; left: 0; width: 362px; top: 670px; text-align: center; font-size: 12px; color: var(--teal); }

  .mountains { position: absolute; left: 0; bottom: 0; width: 1046px; height: 62px; background: linear-gradient(180deg, var(--mountain-top) 0%, #9fb8d6 50%, var(--mountain-base) 100%); }

  /* Services */
  .services-title { left: 475px; top: 60px; width: 176px; height: 36px; line-height: 36px; font-size: 21px; z-index: 2; }
  .services-sub { position: absolute; left: 640px; top: 56px; width: 240px; height: 30px; border: 2px solid var(--teal); border-radius: 16px; color: var(--ink); font-size: 13px; line-height: 26px; padding-left: 38px; }

  .photo { position: absolute; border-radius: 18px; width: 168px; height: 120px; }
  .photo.gym { background: linear-gradient(135deg, #cfe2ee, #6f93ad); }
  .photo.spine { background: linear-gradient(135deg, #eef2f6, #6f8fb8); }
  .photo.massage { background: linear-gradient(135deg, #c99a7a, #6a3f2c); }
  .photo.limb { background: linear-gradient(135deg, #f0f0f0, #8d8d8d); }
  .photo.neck { background: linear-gradient(135deg, #f2e2d5, #b88d70); }
  .photo.smile { background: linear-gradient(135deg, #fbf3ee, #e2c3b1); }

  .service { position: absolute; height: 42px; }
  .service .icon { position: absolute; left: 0; top: 1px; width: 40px; height: 40px; }
  .service .bar { position: absolute; left: 46px; top: 0; height: 42px; background: var(--teal); color: #fff; padding: 5px 8px 0 8px; white-space: nowrap; }
  .service .kicker { display: block; font-size: 11.5px; line-height: 14px; }
  .service .name { display: block; font-size: 14px; font-weight: 500; line-height: 19px; letter-spacing: .2px; }
</style>
</head>
<body>
  <main class="brochure">
    <div class="fold" style="left:362px"></div>
    <div class="fold" style="left:690px"></div>

    <!-- Left panel -->
    <p class="welcome">WELCOME TO</p>
    <p class="brand-name">TAVREN</p>
    <p class="brand-sub">CHIROPRACTIC</p>

    <section class="values">
      <h2>OUR VALUES</h2>
      <p>Tavren Chiropractic was founded to deliver a mobile top end service for the management of acute and chronic soft tissue injuries. Our business model was chosen to allow quality over quantity. Tavren Chiropractic will take the time to do the right examination and match it with the best available evidence for gentle conservative care and management of acute and chronic injuries. Your time is precious in Kaldren and by coming to you we hope you can spend it more efficiently.</p>
    </section>

    <div class="pill give-title">WE GIVE YOU</div>
    <div class="benefits">
      <div class="benefit care">
        <svg width="26" height="26" viewBox="0 0 26 26"><circle cx="13" cy="13" r="13" fill="var(--teal-light)"/><path d="M13 19s-6-3.6-6-7.6A3.3 3.3 0 0 1 13 9.6a3.3 3.3 0 0 1 6 1.8C19 15.4 13 19 13 19z" fill="none" stroke="var(--teal)" stroke-width="1.6"/></svg>
        PATIENT<br>CENTERED<br>CARE
      </div>
      <div class="benefit timing">
        <svg width="26" height="26" viewBox="0 0 26 26"><circle cx="13" cy="13" r="13" fill="var(--teal-light)"/><circle cx="13" cy="13" r="6.5" fill="none" stroke="var(--teal)" stroke-width="1.6"/><path d="M13 9.5V13l2.5 2" fill="none" stroke="var(--teal)" stroke-width="1.6"/></svg>
        ON TIME<br>SERVICE<br>DELIVERY
      </div>
      <div class="benefit quality">
        <svg width="26" height="26" viewBox="0 0 26 26"><circle cx="13" cy="13" r="13" fill="var(--teal-light)"/><path d="M13 6l6 2.4v4.4c0 3.6-2.7 5.9-6 7.2-3.3-1.3-6-3.6-6-7.2V8.4z" fill="none" stroke="var(--teal)" stroke-width="1.6"/><path d="M10 13l2 2 4-4" fill="none" stroke="var(--teal)" stroke-width="1.6"/></svg>
        JAPANESE REGISTERED<br>AND INSURED<br>QUALITY SERVICE
      </div>
    </div>

    <div class="book-band">
      <div class="rule" style="left:6px;width:110px"></div>
      <div class="rule" style="left:256px;width:100px"></div>
      <div class="label">TO BOOK ONLINE</div>
    </div>
    <p class="book-text">Please call your reception to arrange<br>a time or you can book online at</p>
    <p class="book-link">www.tavrenchiropractic.com/appointments/</p>

    <!-- Services header -->
    <div class="services-sub">Just a few of our services</div>
    <div class="pill services-title">OUR SERVICES</div>

    <!-- Column one -->
    <div class="photo gym" style="left:428px;top:114px" role="img" aria-label="Photo of patients doing strength exercises in a gym"></div>
    <div class="service" style="left:386px;top:246px">
      <svg class="icon" viewBox="0 0 40 40"><circle cx="20" cy="20" r="18" fill="none" stroke="var(--teal)" stroke-width="2"/><path d="M20 28s-8-4.8-8-10a4.4 4.4 0 0 1 8-2.4 4.4 4.4 0 0 1 8 2.4c0 5.2-8 10-8 10z" fill="none" stroke="var(--teal)" stroke-width="1.8"/><path d="M13 20h4l2-3 2 5 2-2h4" fill="none" stroke="var(--teal)" stroke-width="1.5"/></svg>
      <div class="bar" style="width:226px"><span class="kicker">Building strength and stability</span><span class="name">REHABILITATION</span></div>
    </div>

    <div class="photo spine" style="left:428px;top:312px" role="img" aria-label="Photo of a chiropractor adjusting a patient's spine"></div>
    <div class="service" style="left:386px;top:441px">
      <svg class="icon" viewBox="0 0 40 40"><circle cx="20" cy="20" r="18" fill="none" stroke="var(--teal)" stroke-width="2"/><circle cx="20" cy="11.5" r="2.6" fill="var(--teal)"/><path d="M12 16h16M20 16v7M20 23l-4 7M20 23l4 7" fill="none" stroke="var(--teal)" stroke-width="2" stroke-linecap="round"/></svg>
      <div class="bar" style="width:226px"><span class="kicker">Traditional Chiropractic</span><span class="name">SPINAL ADJUSTEMENTS</span></div>
    </div>

    <div class="photo massage" style="left:428px;top:504px" role="img" aria-label="Photo of hands massaging a patient's back"></div>
    <div class="service" style="left:386px;top:633px">
      <svg class="icon" viewBox="0 0 40 40"><circle cx="20" cy="20" r="18" fill="none" stroke="var(--teal)" stroke-width="2"/><path d="M13 22v-7a1.5 1.5 0 0 1 3 0v5M16 20v-8a1.5 1.5 0 0 1 3 0v8M19 20v-7a1.5 1.5 0 0 1 3 0v7M22 20v-5a1.5 1.5 0 0 1 3 0v8c0 3-2 5-5.5 5S13 26 13 22" fill="none" stroke="var(--teal)" stroke-width="1.5"/></svg>
      <div class="bar" style="width:226px"><span class="kicker">Muscle fatigue and injury</span><span class="name">SOFT TISSUE RELEASE WORK</span></div>
    </div>

    <!-- Column two -->
    <div class="photo limb" style="left:757px;top:106px" role="img" aria-label="Photo of a therapist mobilising a patient's leg"></div>
    <div class="service" style="left:718px;top:240px">
      <svg class="icon" viewBox="0 0 40 40"><circle cx="20" cy="20" r="18" fill="none" stroke="var(--teal)" stroke-width="2"/><path d="M12 26l6-6 3 3 7-9M24 14h4v4" fill="none" stroke="var(--teal)" stroke-width="1.8" stroke-linecap="round"/></svg>
      <div class="bar" style="width:226px"><span class="kicker">Modern developments</span><span class="name">PERIPHERAL MOBILISATIONS</span></div>
    </div>

    <div class="photo neck" style="left:757px;top:300px" role="img" aria-label="Photo of a therapist treating a patient's neck and shoulders"></div>
    <div class="service" style="left:718px;top:434px">
      <svg class="icon" viewBox="0 0 40 40"><circle cx="20" cy="20" r="18" fill="none" stroke="var(--teal)" stroke-width="2"/><circle cx="20" cy="11.5" r="2.6" fill="var(--teal)"/><path d="M12 16h16M20 16v7M20 23l-4 7M20 23l4 7" fill="none" stroke="var(--teal)" stroke-width="2" stroke-linecap="round"/></svg>
      <div class="bar" style="width:226px"><span class="kicker">Traditional Chiropractic</span><span class="name">SPINAL ADJUSTEMENTS</span></div>
    </div>

    <div class="photo smile" style="left:757px;top:496px" role="img" aria-label="Close-up photo of a smiling patient holding their jaw"></div>
    <div class="service" style="left:718px;top:634px">
      <svg class="icon" viewBox="0 0 40 40"><circle cx="20" cy="20" r="18" fill="none" stroke="var(--teal)" stroke-width="2"/><path d="M13 22v-7a1.5 1.5 0 0 1 3 0v5M16 20v-8a1.5 1.5 0 0 1 3 0v8M19 20v-7a1.5 1.5 0 0 1 3 0v7M22 20v-5a1.5 1.5 0 0 1 3 0v8c0 3-2 5-5.5 5S13 26 13 22" fill="none" stroke="var(--teal)" stroke-width="1.5"/></svg>
      <div class="bar" style="width:226px"><span class="kicker">Traditional Chiropractic</span><span class="name">SPINAL ADJUSTEMENTS</span></div>
    </div>

    <div class="mountains" role="img" aria-label="Illustration of snow-capped blue mountain range along the bottom edge"></div>
  </main>
</body>
</html>
```